Safety Brochure for Industry Assocations

This is an 8.5 x 11 single sided brochure for our Occupational Health and Safety Data Analytics software. If you need to use stock images we will pay for them.

Please incorporate our logo and some of the images. No need to incorporate them all. We like the idea of the boots being at the bottom of the page but we're open to other ideas.

Please note that we intend to mail this brochure to different industries so it should be generic (i.e. not construction specific).

Target Market(s)

Safety and Industry Organisations for construction, mining, forestry and oil and gas industries.

Industry/Entity Type

Industry

Font styles to use
Sans Serif

Colors

Designer to choose colors to be used in the design.

Requirements
Must have
• We are a software company that produces safety software. Our customers are companies that engage in dangerous work and use our software to improve their worker's safety. The look and feel should convey the fact that:
• -We are Big Data
• -We are Software
• -We service industry
Nice to have
• Please see the Pixlore photo of the boots. We were hoping that the desiger would be able ti modify the image with an overlay of 0's and 1's in a kind of "matrix" fashion to indicate that we are merging traditional labour work with software.
Should not have
• No medical symbols. Note that WE ARE NOT HEALTH CARE.

```html
<!DOCTYPE html>
<html lang="en">
<head>
<meta charset="utf-8">
<title>Ridgeline Analytics – Leverage The Power of Big Data</title>
<link href="https://fonts.googleapis.com/css2?family=Hind:wght@400;500;600;700&family=Roboto+Condensed:wght@300;400&family=Roboto:wght@700;900&display=swap" rel="stylesheet">
<style>
  :root{
    --green:#0e9a48;
    --green-dark:#0b7f3b;
    --ink:#2f3133;
    --charcoal:#3d3f41;
    --panel-grey:#eeeff0;
    --card-top:#f4f4f4;
    --card-bottom:#cfd0d1;
    --page:#e9e7e3;
    --white:#ffffff;
  }
  *{box-sizing:border-box;margin:0;padding:0}
  html,body{width:1200px;height:1200px;overflow:hidden;background:var(--page)}
  body{font-family:"Hind",sans-serif;color:var(--ink)}
  .flyer{position:absolute;left:167px;top:40px;width:866px;height:1120px;background:var(--white);overflow:hidden;box-shadow:0 2px 10px rgba(0,0,0,.12)}
  .hero-shapes{position:absolute;left:0;top:0}
  .brand{position:absolute;left:128px;top:78px;display:flex;align-items:center;gap:12px;z-index:1}
  .brand-dot{width:48px;height:48px;border-radius:50%;background:var(--green)}
  .brand-name{font-family:"Hind",sans-serif;font-weight:600;font-size:25px;color:var(--ink);letter-spacing:1px}
  .headline-lead{position:absolute;left:42px;top:172px;font-family:"Roboto Condensed",sans-serif;font-weight:400;font-size:43px;color:var(--green);white-space:nowrap;letter-spacing:-.5px;z-index:1}
  .headline-main{position:absolute;left:40px;top:214px;font-family:"Roboto",sans-serif;font-weight:900;font-size:86px;color:var(--ink);white-space:nowrap;letter-spacing:1px;z-index:1}
  .feature{position:absolute;top:459px;width:229px}
  .feature-icon{display:block;margin:0 auto;height:56px}
  .feature-card{position:relative;margin-top:10px;height:136px;border:2px solid var(--green);border-radius:12px;background:linear-gradient(180deg,var(--card-top),var(--card-bottom));text-align:center;padding-top:30px}
  .feature-label{position:absolute;left:50%;top:-16px;transform:translateX(-50%);background:var(--green);color:var(--white);font-family:"Hind",sans-serif;font-weight:700;font-size:20px;line-height:32px;padding:0 14px;border-radius:12px;white-space:nowrap}
  .feature-card p{font-size:13px;font-weight:500;line-height:1.25;margin-bottom:11px;color:var(--ink)}
  .lower{position:absolute;left:0;top:689px;width:866px;height:431px;background:var(--panel-grey);border-top:4px solid var(--charcoal)}
  .intro{position:absolute;left:68px;top:18px;width:405px;font-size:12.6px;line-height:15px;color:var(--ink)}
  .pillar{position:absolute;top:110px;height:46px;border:2px solid var(--green);border-radius:12px;background:var(--white);font-weight:600;font-size:14.5px;text-align:center;line-height:50px;white-space:nowrap}
  .pillar-num{position:absolute;left:50%;top:-27px;transform:translateX(-50%);width:36px;height:36px;border-radius:50%;background:var(--green);color:var(--white);font-weight:700;font-size:26px;line-height:40px;text-align:center;border:2px solid var(--white)}
  .boots-photo{position:absolute;left:28px;top:188px;width:442px;height:220px}
  .benefits{position:absolute;left:524px;top:-20px;width:299px;height:362px;background:linear-gradient(180deg,var(--green),var(--green-dark));border-top-left-radius:18px;padding:64px 16px 0 22px}
  .benefits li{list-style:none;position:relative;padding-left:26px;color:var(--white);font-weight:500;font-size:15px;line-height:19px;padding-bottom:10px;margin-bottom:12px}
  .benefits li::after{content:"";position:absolute;left:26px;right:20px;bottom:0;border-bottom:1px solid rgba(255,255,255,.75)}
  .benefits li:last-child::after{display:none}
  .benefits svg{position:absolute;left:0;top:2px}
  .contact-bar{position:absolute;left:453px;top:343px;width:413px;height:63px;background:var(--charcoal);padding:9px 0 0 88px;color:var(--white);font-weight:600;font-size:14.5px;line-height:21px}
  .contact-bar div{display:flex;align-items:center;gap:12px}
</style>
</head>
<body>
<main class="flyer">
  <svg class="hero-shapes" width="866" height="640" viewBox="0 0 866 640">
    <polygon points="0,314 343,416 520,334 520,341 343,425 0,324" fill="var(--charcoal)"/>
    <polygon points="0,302 343,404 520,322 520,334 343,416 0,314" fill="var(--green)"/>
    <defs>
      <radialGradient id="heroGlow" cx="0.5" cy="0.42" r="0.6">
        <stop offset="0" stop-color="#4aa8e6"/>
        <stop offset="0.35" stop-color="#1f5e9c"/>
        <stop offset="0.7" stop-color="#6e7478"/>
        <stop offset="1" stop-color="#2c2f33"/>
      </radialGradient>
    </defs>
    <circle cx="703" cy="195" r="240" fill="var(--green)"/>
    <circle cx="703" cy="195" r="228" fill="url(#heroGlow)" role="img" aria-label="Photo of a hand holding a glowing globe of data screens"/>
  </svg>

  <div class="brand"><span class="brand-dot"></span><span class="brand-name">Ridgeline Analytics</span></div>
  <h2 class="headline-lead">Leverage The Power of</h2>
  <h1 class="headline-main">BIG DATA</h1>

  <section class="feature" style="left:65px">
    <svg class="feature-icon" viewBox="0 0 56 56" width="56" height="56">
      <circle cx="10" cy="6" r="5" fill="var(--green)"/>
      <rect x="5" y="13" width="10" height="22" fill="var(--green)"/>
      <rect x="5" y="35" width="4" height="18" fill="var(--green)"/><rect x="11" y="35" width="4" height="18" fill="var(--green)"/>
      <rect x="15" y="15" width="16" height="4" fill="var(--green)"/>
      <rect x="22" y="6" width="28" height="24" fill="none" stroke="var(--green)" stroke-width="4"/>
      <path d="M28 30 L22 53 M44 30 L50 53" stroke="var(--green)" stroke-width="4"/>
    </svg>
    <div class="feature-card"><span class="feature-label">TRAINING</span>
      <p>Analyze Needs of Industry</p><p>Deliver Proactive Training</p><p>Improve Safety</p></div>
  </section>

  <section class="feature" style="left:318px">
    <svg class="feature-icon" viewBox="0 0 56 56" width="56" height="56">
      <circle cx="28" cy="30" r="23" fill="none" stroke="var(--green)" stroke-width="2.5"/>
      <rect x="24" y="3" width="8" height="4" fill="var(--green)"/>
      <path d="M20 22 L30 32 L34 36 L26 28Z" stroke="var(--green)" stroke-width="3"/>
      <circle cx="28" cy="30" r="2" fill="var(--green)"/>
    </svg>
    <div class="feature-card" style="padding-top:24px"><span class="feature-label">BENCHMARKING</span>
      <p>Engage with Members</p><p>Promote Collaborative<br>Advancement of Safety</p><p>Improve Safety</p></div>
  </section>

  <section class="feature" style="left:571px">
    <svg class="feature-icon" viewBox="0 0 56 56" width="56" height="56">
      <rect x="2" y="30" width="7" height="24" fill="var(--green)"/><rect x="13" y="36" width="7" height="18" fill="var(--green)"/>
      <rect x="24" y="26" width="7" height="28" fill="var(--green)"/><rect x="35" y="22" width="7" height="32" fill="var(--green)"/>
      <rect x="46" y="8" width="7" height="46" fill="var(--green)"/>
      <polyline points="5,22 16,28 27,16 38,18 50,3" fill="none" stroke="var(--green)" stroke-width="2"/>
      <circle cx="16" cy="28" r="3" fill="var(--white)" stroke="var(--green)" stroke-width="2"/><circle cx="27" cy="16" r="3" fill="var(--white)" stroke="var(--green)" stroke-width="2"/><circle cx="50" cy="3" r="3" fill="var(--white)" stroke="var(--green)" stroke-width="2"/>
    </svg>
    <div class="feature-card"><span class="feature-label">TREND ANALYSIS</span>
      <p>Monitor Industry Trends</p><p>Implement Corrective Initiatives</p><p>Improve Safety</p></div>
  </section>

  <section class="lower">
    <p class="intro">We are a software company that produces safety software. Our customers are companies that engage in dangerous work and use our software to improve their worker's safety. The look and feel should convey the fact that:</p>
    <div class="pillar" style="left:62px;width:127px"><span class="pillar-num">1</span>We are Big Data</div>
    <div class="pillar" style="left:192px;width:129px"><span class="pillar-num">2</span>We are Software</div>
    <div class="pillar" style="left:325px;width:147px"><span class="pillar-num">3</span>We Service Industry</div>
    <svg class="boots-photo" viewBox="0 0 442 220" role="img" aria-label="Photo of worn leather work boots with a binary code overlay">
      <defs><radialGradient id="bootTone" cx="0.5" cy="0.55" r="0.55"><stop offset="0" stop-color="#6b4a30"/><stop offset="0.7" stop-color="#4a3426"/><stop offset="1" stop-color="#eeeff0"/></radialGradient></defs>
      <ellipse cx="221" cy="115" rx="221" ry="110" fill="url(#bootTone)"/>
    </svg>
    <ul class="benefits">
      <li><svg width="14" height="14" viewBox="0 0 14 14"><circle cx="7" cy="7" r="5.5" fill="none" stroke="#fff" stroke-width="1.4"/><path d="M4 7 L6.3 9.2 L12 3" fill="none" stroke="#fff" stroke-width="1.6"/></svg>LEAD the next wave of injury reduction</li>
      <li><svg width="14" height="14" viewBox="0 0 14 14"><circle cx="7" cy="7" r="5.5" fill="none" stroke="#fff" stroke-width="1.4"/><path d="M4 7 L6.3 9.2 L12 3" fill="none" stroke="#fff" stroke-width="1.6"/></svg>ENGAGE with members through collaboration &amp; benchmarking</li>
      <li><svg width="14" height="14" viewBox="0 0 14 14"><circle cx="7" cy="7" r="5.5" fill="none" stroke="#fff" stroke-width="1.4"/><path d="M4 7 L6.3 9.2 L12 3" fill="none" stroke="#fff" stroke-width="1.6"/></svg>PROMOTE standardization</li>
      <li><svg width="14" height="14" viewBox="0 0 14 14"><circle cx="7" cy="7" r="5.5" fill="none" stroke="#fff" stroke-width="1.4"/><path d="M4 7 L6.3 9.2 L12 3" fill="none" stroke="#fff" stroke-width="1.6"/></svg>ANALYZE Accurate, Timely and Complete Leading Indicators</li>
      <li><svg width="14" height="14" viewBox="0 0 14 14"><circle cx="7" cy="7" r="5.5" fill="none" stroke="#fff" stroke-width="1.4"/><path d="M4 7 L6.3 9.2 L12 3" fill="none" stroke="#fff" stroke-width="1.6"/></svg>TRAIN industry more proactively</li>
    </ul>
    <div class="contact-bar">
      <div><svg width="14" height="14" viewBox="0 0 14 14"><path d="M3 1 L5.5 1 L6.5 4 L5 5.5 Q6.5 8.5 8.5 9 L10 7.5 L13 8.5 L13 11 Q12 13 10 13 Q2 11 1 3 Q1 1 3 1Z" fill="var(--green)"/></svg>1-888-555-0142</div>
      <div><svg width="14" height="14" viewBox="0 0 14 14"><circle cx="7" cy="7" r="6" fill="var(--green)"/><path d="M1 7 H13 M7 1 Q3 7 7 13 M7 1 Q11 7 7 13" fill="none" stroke="var(--charcoal)" stroke-width="1"/></svg>www.ridgelineanalytics.com</div>
    </div>
  </section>
</main>
</body>
</html>
```